Real Estate Business Cards

Looking for a clean, sharp and professional look for our Real Estate investment Fund that invests in Multi Family Apartment buildings.

Target Market(s)

Real Estate Fund

Industry/Entity Type

Real Estate

Contact Information for Business Card

Company Description: Real Estate Investment Fund
Company Name: RKW Holdings
Name: Marcus Olvane
Cell: (917) 482-0657
Email: marcus@rkwholdings-example.com
Website: www.rkwholdings-example.com
Address: 418, 9th Street, Brooklyn NY 11218

Colors

Designer to choose colors to be used in the design.

Requirements
Nice to have
• Colors to match logo

```html
<!DOCTYPE html>
<html lang="en">
<head>
<meta charset="utf-8">
<title>RKW Holdings — Business Card</title>
<link rel="stylesheet" href="https://fonts.googleapis.com/css2?family=Arimo:wght@400;700&family=Cinzel:wght@400&display=swap">
<style>
  :root {
    --backdrop: #2a2e34;
    --card-charcoal: #4a4a4c;
    --card-charcoal-light: #505052;
    --card-white: #ffffff;
    --brand-blue: #1a6aa8;
    --ink-dark: #3e3e41;
    --text-light: #ffffff;
  }
  * { box-sizing: border-box; margin: 0; padding: 0; }
  html, body {
    width: 1200px; height: 1000px; overflow: hidden;
    background: var(--backdrop);
  }
  .canvas {
    position: relative; width: 1200px; height: 1000px;
  }
  .card {
    position: absolute; left: 220px; width: 760px; height: 434px;
    border-radius: 22px; overflow: hidden;
    background: var(--card-charcoal);
    box-shadow: 0 18px 40px rgba(0,0,0,0.45);
  }
  .card--back { top: 48px; }
  .card--front { top: 518px; }

  /* Back */
  .back-pattern {
    position: absolute; inset: 0;
    background: linear-gradient(135deg, var(--card-charcoal-light), var(--card-charcoal));
  }
  .back-wordmark {
    position: absolute; left: 0; right: 0; top: 50%;
    transform: translateY(-50%);
    text-align: center;
    font-family: "Cinzel", serif; font-weight: 400;
    font-size: 40px; letter-spacing: 3px;
    color: var(--text-light);
  }

  /* Front */
  .front-shape { position: absolute; inset: 0; }
  .identity { position: absolute; left: 62px; top: 58px; }
  .identity__name {
    font-family: "Arimo", sans-serif; font-weight: 700;
    font-size: 31px; letter-spacing: 0.5px;
    color: var(--brand-blue); text-transform: uppercase;
  }
  .identity__role {
    margin-top: 6px;
    font-family: "Arimo", sans-serif; font-weight: 400;
    font-size: 21px; color: var(--text-light);
  }
  .identity__rule {
    margin-top: 10px; width: 44px; height: 3px;
    background: var(--brand-blue);
  }
  .contact {
    position: absolute; left: 62px; top: 252px;
    font-family: "Arimo", sans-serif; font-size: 18px;
    color: var(--text-light); line-height: 1.35;
  }
  .contact__address { margin-left: 28px; margin-bottom: 6px; }
  .contact__row { display: flex; align-items: center; gap: 10px; margin-bottom: 6px; }
  .contact__icon { width: 18px; height: 18px; flex: none; }
  .front-wordmark {
    position: absolute; left: 440px; width: 320px; top: 196px;
    text-align: center;
    font-family: "Cinzel", serif; font-weight: 400;
    font-size: 30px; letter-spacing: 2px;
    color: var(--ink-dark);
  }
</style>
</head>
<body>
<main class="canvas">

  <section class="card card--back" aria-label="Card back">
    <div class="back-pattern" role="img" aria-label="Subtle tone-on-tone repeating brand pattern"></div>
    <div class="back-wordmark">RKW Holdings</div>
  </section>

  <section class="card card--front" aria-label="Card front">
    <svg class="front-shape" width="760" height="434" viewBox="0 0 760 434" aria-hidden="true">
      <polygon points="542,0 402,250 486,434 760,434 760,0" fill="var(--card-white)" stroke="var(--card-white)" stroke-width="6" stroke-linejoin="round"/>
      <polygon points="550,0 412,250 494,434 760,434 760,0" fill="var(--brand-blue)" stroke="var(--brand-blue)" stroke-width="4" stroke-linejoin="round"/>
      <polygon points="562,0 424,250 506,434 760,434 760,0" fill="var(--card-white)" stroke="var(--card-white)" stroke-width="4" stroke-linejoin="round"/>
    </svg>

    <div class="identity">
      <div class="identity__name">Marcus Olvane</div>
      <div class="identity__role">CEO</div>
      <div class="identity__rule"></div>
    </div>

    <div class="contact">
      <div class="contact__address">418, 9th Street,<br>Brooklyn NY 11218</div>
      <div class="contact__row">
        <svg class="contact__icon" viewBox="0 0 24 24" aria-hidden="true"><path fill="var(--brand-blue)" d="M6.6 10.8a15 15 0 0 0 6.6 6.6l2.2-2.2a1 1 0 0 1 1-.25 11.4 11.4 0 0 0 3.6.57 1 1 0 0 1 1 1V20a1 1 0 0 1-1 1A17 17 0 0 1 3 4a1 1 0 0 1 1-1h3.5a1 1 0 0 1 1 1c0 1.25.2 2.45.57 3.6a1 1 0 0 1-.25 1z"/></svg>
        <span>(917) 482-0657</span>
      </div>
      <div class="contact__row">
        <svg class="contact__icon" viewBox="0 0 24 24" aria-hidden="true"><rect x="2" y="5" width="20" height="14" rx="1.5" fill="var(--brand-blue)"/><path d="M3 6l9 7 9-7" fill="none" stroke="#cfe1f0" stroke-width="1.6"/></svg>
        <span>marcus@rkwholdings-example.com</span>
      </div>
      <div class="contact__row">
        <svg class="contact__icon" viewBox="0 0 24 24" aria-hidden="true"><circle cx="12" cy="12" r="10" fill="var(--brand-blue)"/><path d="M2 12h20M12 2c3 3 3 17 0 20M12 2c-3 3-3 17 0 20" fill="none" stroke="#cfe1f0" stroke-width="1.3"/></svg>
        <span>www.rkwholdings-example.com</span>
      </div>
    </div>

    <div class="front-wordmark">RKW Holdings</div>
  </section>

</main>
</body>
</html>
```